energy rating company

Web Design graphics and layout only

To create two pages for the website. First the home page and the second is the design for the job board for our clients use after login. I have attached files that explain in detail what the pages should have and the purpose/desires of each object. Please read these thoroughly.

The webpages need to be clean, professional, easy on the eye, obvious in all its buttons and functions with a strong call to action on the home page and branding and clean, great and obvious looking buttons and very simple but dynamic as well. We wish to be seen as contemporary.

Business Concept

Our business concept is simple, to build a website whereby our clients will be able to upload jobs for energy raters to quote on and subsequent complete the work if their quote is selected. To link energy ratings that are required with energy raters via our website. Similarly to the varlo website, jobs will be “advertised” on the job board and raters will select which jobs they wish to quote for.

I have attached a Word document explaining all the parts of the website and another word document showing what we are sort of after and a excel spreadsheet as well. Please read these in conjunction with this brief!
Updates

Dear All

I have submitted with my brief a word doc and excel spreadsheet of the two pages I want created.  However this is not the layout or design I want, I only put it together so that you will need to know what is required on each page.  Feel free to change and redesign it all.

Also the second page does not require the "process" logo or any other menu items except the first five being Home, How it works, About Us, testimonials and Contact us as per the home page.

We also are looking for something very professional and very clean.  It should be very easy to see exactly what you are looking for.

I will also extend the deadline for new designers!!  I am excited to see your talents!!

Thanks

I have increase budget and posted a note saying feel free to change all the details layout etc on my brief just include everything!!! 

Wanting a professional corporate look...

Want a professional corporate look

We have changed our minds and you we no longer require the process to be on the home page.

Thanks

Target Market(s)

Target Market

Home Inspection Companies
Pest Inspection Companies
Residential home buyers/sellers
Real Estate companies

Industry/Entity Type

It Company

Number of Pages Required

1 page

Requirements
Must have
• Colours and Styles

• The website should be mainly white as I believe it is seen as clean and simple with colour from the logos, but can be swayed if it projects the image we are after.

• It should be obvious and process orientated and I do believe symbols, pictures, etc should replace words where possible.

```html
<!DOCTYPE html>
<html lang="en">
<head>
<meta charset="utf-8">
<title>Ratewise Australia – Energy Rating Quotes</title>
<link href="https://fonts.googleapis.com/css2?family=Open+Sans:wght@400;600;700&display=swap" rel="stylesheet">
<style>
:root{
  --brown:#b5561b;
  --brown-text:#c25a1c;
  --green:#1f8d3b;
  --red:#e0101e;
  --ink:#222;
  --grey:#555;
  --step-bg:#f7dccb;
  --line:#d8d8d8;
}
*{box-sizing:border-box;margin:0;padding:0}
html,body{width:1138px;height:1200px;overflow:hidden}
body{font-family:"Open Sans",Arial,sans-serif;color:var(--ink);background:#fff;position:relative}
a{color:inherit;text-decoration:none}

.site-header{position:absolute;left:0;top:0;width:1138px;height:126px;background:linear-gradient(#fff,#f1f1f1)}
.header-rule{position:absolute;left:0;top:126px;width:1138px;height:8px;background:var(--green)}
.top-nav{position:absolute;left:535px;top:3px;font-size:14px;color:#111}
.top-nav span{margin:0 3px}
.account-links{position:absolute;left:940px;top:3px;font-size:14px}
.forgot{position:absolute;left:972px;top:22px;font-size:10px;color:#888;text-decoration:underline}

.brand{position:absolute;left:50px;top:44px;display:flex;align-items:center;gap:12px}
.brand-dot{width:70px;height:70px;border-radius:50%;background:var(--brown)}
.brand-name{font-size:40px;font-weight:700;color:var(--brown);line-height:1}

.main-tabs{position:absolute;left:538px;top:69px;display:flex;gap:4px}
.tab{width:175px;height:53px;background:var(--brown);color:#fff;display:flex;flex-direction:column;justify-content:center;align-items:center;font-size:17px;line-height:1.1;text-align:center;position:relative}
.tab small{font-size:11px;margin-top:3px}
.tab.active::after{content:"";position:absolute;bottom:-1px;left:80px;border:7px solid transparent;border-bottom-color:#fff}

.steps-band{position:absolute;left:0;top:134px;width:1138px;height:476px;background:linear-gradient(#fff,#f3f3f3)}
.steps-title{position:absolute;left:72px;top:180px;font-size:23px;line-height:1.2;color:var(--brown-text)}
.steps-title b{color:var(--green)}
.steps{position:absolute;left:257px;top:167px;display:flex;gap:6px}
.step{width:155px;height:87px;background:var(--step-bg);position:relative;overflow:hidden;border:2px solid #fbeee6}
.step-num{position:absolute;left:4px;top:6px;font-size:84px;font-weight:700;color:#fff;line-height:1}
.step-label{position:absolute;left:47px;top:22px;font-size:14px;line-height:1.05;color:var(--brown-text)}

.hero{position:absolute;left:50px;top:276px;width:1019px;height:316px;border:1px solid #ccc;border-radius:8px;background:linear-gradient(#fff 75%,#eee)}
.hero-copy{position:absolute;left:35px;top:30px;width:700px;font-size:21px;line-height:1.38;color:#444}
.hero-copy .name{color:var(--brown);font-weight:700}
.hero-copy .accent{color:var(--brown-text);margin-top:4px}
.hero-cta{font-size:27px;line-height:1.1;margin-top:20px;color:#333}
.hero-cta b{color:var(--red)}
.hero-visual{position:absolute;left:817px;top:30px;width:150px;height:255px;border-radius:75px 75px 30px 30px;background:radial-gradient(circle at 50% 35%,#f6f6f6,#d7d7d7 70%,#9a9a9a)}

.features{position:absolute;left:58px;top:641px;width:662px;height:292px;border:1px solid #ccc;border-radius:8px;background:#fff;padding:20px 0 0 30px}
.features li{list-style:none;font-size:14px;height:26.7px;display:flex;align-items:center;gap:16px}
.features svg{flex:none}
.closing{position:absolute;left:58px;top:957px;font-size:14px;line-height:1}
.closing p{margin-bottom:15px}
.closing a{color:var(--red);text-decoration:underline}

.testimonials{position:absolute;left:778px;top:622px;width:277px;height:417px;background:linear-gradient(90deg,#f7f7f7,#fff 30%)}
.testimonials h2{font-size:18px;font-weight:400;color:#333;margin:8px 0 0 43px}
.bubble{position:absolute;left:45px;top:7px}
.quote{position:relative;padding:0 0 0 45px;margin-top:18px}
.quote-mark{position:absolute;left:46px;top:0;width:62px;height:62px;border-radius:50%;background:#dcdcdc}
.quote-head{margin-left:92px;font-size:12px;color:#333;line-height:1.2}
.quote-head strong{display:block;font-size:16px;font-weight:400;margin-bottom:4px}
.quote-head span{display:block;color:#888;font-size:10px}
.quote p{font-size:12px;color:#444;line-height:1.35;margin:20px 20px 0 0}
.divider{margin:16px 0 0 45px;width:210px;border-top:1px solid var(--line)}
.more{position:absolute;left:45px;top:395px;font-size:12px;color:var(--brown-text)}

.footer-rule{position:absolute;left:0;top:1059px;width:1138px;height:13px;background:var(--green)}
.site-footer{position:absolute;left:0;top:1072px;width:1138px;height:128px;background:var(--brown);color:#f4d6c4}
.footer-nav{position:absolute;left:13px;top:13px;font-size:14px}
.footer-brand{position:absolute;left:462px;top:15px;display:flex;align-items:center;gap:9px}
.footer-brand .brand-dot{width:52px;height:52px;background:#fff}
.footer-brand .brand-name{font-size:28px;color:#fff}
.copyright{position:absolute;left:711px;top:9px;font-size:14px}
</style>
</head>
<body>
<header class="site-header">
  <nav class="top-nav"><a href="#">Home</a><span>|</span><a href="#">How it works</a><span>|</span><a href="#">About Us</a><span>|</span><a href="#">Testimonials</a><span>|</span><a href="#">Contact Us</a></nav>
  <div class="account-links">( <a href="#">Login</a> | <a href="#">Register</a>)</div>
  <a class="forgot" href="#">Forget password</a>
  <div class="brand"><span class="brand-dot"></span><span class="brand-name">Ratewise Australia</span></div>
  <nav class="main-tabs">
    <a class="tab active" href="#">Get a quote</a>
    <a class="tab" href="#">Energy Raters<small>(Add your busines)</small></a>
    <a class="tab" href="#">Active<br>Job Board</a>
  </nav>
</header>
<div class="header-rule"></div>

<section class="steps-band"></section>
<div class="steps-title">It’s only took<br><b>5 simple</b> steps</div>
<ol class="steps">
  <li class="step"><span class="step-num">1</span><span class="step-label">Post a<br>Job</span></li>
  <li class="step"><span class="step-num">2</span><span class="step-label">Get As many<br>Quotes as<br>you like</span></li>
  <li class="step"><span class="step-num">3</span><span class="step-label">Select Energy<br>Quote that<br>suits</span></li>
  <li class="step"><span class="step-num">4</span><span class="step-label">Approve<br>Payment</span></li>
  <li class="step"><span class="step-num">5</span><span class="step-label">Receive<br>Rating</span></li>
</ol>

<section class="hero">
  <div class="hero-copy">
    <p><span class="name">Ratewise Australia</span> is Australia’s leading professional energy rating consultancy firm specializing in large scaled residential and commercial energy rating logistics.</p>
    <p class="accent">We have professional and accredited energy raters in all States and Territories ready and waiting to provide quotes for and perform &nbsp;your energy rating jobs!</p>
    <p class="hero-cta">It’s <b>FREE, FAST</b> and <b>EASY</b> to use and you get the best price and turnaround time that suits you!!</p>
  </div>
  <div class="hero-visual" role="img" aria-label="Glass light bulb with soil and a green seedling growing inside"></div>
</section>

<ul class="features">
  <li><svg width="16" height="13" viewBox="0 0 16 13"><path d="M1 7l5 5 9-11" fill="none" stroke="#5cc21a" stroke-width="3"/></svg>Get the best priced quotes for your energy ratings</li>
  <li><svg width="16" height="13" viewBox="0 0 16 13"><path d="M1 7l5 5 9-11" fill="none" stroke="#5cc21a" stroke-width="3"/></svg>Save time by listing a job to get many quotes</li>
  <li><svg width="16" height="13" viewBox="0 0 16 13"><path d="M1 7l5 5 9-11" fill="none" stroke="#5cc21a" stroke-width="3"/></svg>Monitor your jobs and quotes on your own job board</li>
  <li><svg width="16" height="13" viewBox="0 0 16 13"><path d="M1 7l5 5 9-11" fill="none" stroke="#5cc21a" stroke-width="3"/></svg>Be notified via email of all new quotes as they come in</li>
  <li><svg width="16" height="13" viewBox="0 0 16 13"><path d="M1 7l5 5 9-11" fill="none" stroke="#5cc21a" stroke-width="3"/></svg>Be able to specify your desired turnaround times</li>
  <li><svg width="16" height="13" viewBox="0 0 16 13"><path d="M1 7l5 5 9-11" fill="none" stroke="#5cc21a" stroke-width="3"/></svg>Accessible anytime and anywhere</li>
  <li><svg width="16" height="13" viewBox="0 0 16 13"><path d="M1 7l5 5 9-11" fill="none" stroke="#5cc21a" stroke-width="3"/></svg>Choose a deadline for energy raters to supply quotes</li>
  <li><svg width="16" height="13" viewBox="0 0 16 13"><path d="M1 7l5 5 9-11" fill="none" stroke="#5cc21a" stroke-width="3"/></svg>Be able to track your jobs and pay online</li>
  <li><svg width="16" height="13" viewBox="0 0 16 13"><path d="M1 7l5 5 9-11" fill="none" stroke="#5cc21a" stroke-width="3"/></svg>Have access to many qualified energy raters in your state</li>
  <li><svg width="16" height="13" viewBox="0 0 16 13"><path d="M1 7l5 5 9-11" fill="none" stroke="#5cc21a" stroke-width="3"/></svg>Provide feedback on energy raters all quoting for your work</li>
</ul>

<div class="closing">
  <p>Its totally free to be registered with us and there is no obligations or hidden catches!</p>
  <p>So if you wish to utilise the amazing opportunity <a href="#">Register Now! </a></p>
  <p>This new website will be going live on the (insert date) so be ready to save some money!</p>
</div>

<aside class="testimonials">
  <svg class="bubble" width="28" height="24" viewBox="0 0 28 24"><path d="M4 2h20a3 3 0 0 1 3 3v10a3 3 0 0 1-3 3H12l-6 5v-5H4a3 3 0 0 1-3-3V5a3 3 0 0 1 3-3z" fill="#5f6b74"/><circle cx="9" cy="10" r="1.6" fill="#fff"/><circle cx="14" cy="10" r="1.6" fill="#fff"/><circle cx="19" cy="10" r="1.6" fill="#fff"/></svg>
  <h2 style="margin-left:80px">Client Testimonials</h2>
  <div class="quote">
    <span class="quote-mark"></span>
    <div class="quote-head"><strong>Brewline</strong>Daniel Reeve,<span>Interactive Design<br>Manager</span></div>
    <p>"I have told everyone you are the best vendor we have worked with. You are fast, know your stuff and customer service is tops."</p>
  </div>
  <div class="divider"></div>
  <div class="quote">
    <span class="quote-mark"></span>
    <div class="quote-head"><strong>Nordtel</strong>Daniel Reeve,<span>Interactive Design<br>Manager</span></div>
    <p>"I have told everyone you are the best vendor we have worked with. You are fast, know your stuff and customer service is tops."</p>
  </div>
  <a class="more" href="#">more testimonials</a>
</aside>

<div class="footer-rule"></div>
<footer class="site-footer">
  <nav class="footer-nav"><a href="#">Home</a> | <a href="#">How it works</a> | <a href="#">About Us</a> | <a href="#">Testimonials</a> | <a href="#">Contact Us</a></nav>
  <div class="footer-brand"><span class="brand-dot"></span><span class="brand-name">Ratewise Australia</span></div>
  <p class="copyright">Copyright © 2010, Ratewise Australia , &nbsp;All Rights Reserved</p>
</footer>
</body>
</html>
```